New cool to-go cup for KELMO Coffee

UPDATE MARCH 18: Please read the attached document "Design ideas - Front" with a mock-up of the design we are looking for. And please don't change the logo.

We are looking for a new cool design for our to-go cups in kraft paper (same style as the attached photo).

The idea:

We have three different cups sizes: 6oz, 8oz and 12oz. We call them “Tiny-Lark” (6oz), “Mid-Wren” (8oz) and “Tall-heron” (12oz) (refers to the size in milliliters). We would like to include this in the cup design. Please see the attached sketch of the idea ("Design ideas - Front").

The backside of the cup should have the attached text and logo ("Design ideas - Back").

But other ideas are also very welcome too! Maybe just a simple cup with the logo.

Please keep the design very minimalistic. The more simple the better.

Target Market(s)

Young urban people

Industry/Entity Type

Coffee shop

Font styles to use
Sans Serif

Requirements
Must have
• Kraft paper cups

```html
<!DOCTYPE html>
<html lang="en">
<head>
<meta charset="utf-8">
<title>KELMO Coffee – to-go cups</title>
<link rel="stylesheet" href="https://fonts.googleapis.com/css2?family=Hind:wght@400;600;700&display=swap">
<style>
  :root {
    --bg-top: #dbc0a7;
    --bg-bottom: #f8ebd2;
    --kraft: #c09f7c;
    --kraft-edge: #b59372;
    --cup-white: #f4f4f2;
    --lid: #3a1a0c;
    --lid-rim: #2a1107;
    --ink: #3a2416;
  }
  html, body {
    margin: 0;
    padding: 0;
    width: 1200px;
    height: 960px;
    overflow: hidden;
  }
  body {
    background: linear-gradient(to bottom, var(--bg-top), var(--bg-bottom));
    font-family: "Hind", sans-serif;
  }
  .cup-lineup { display: block; width: 1200px; height: 960px; }
  .lid-dome { fill: var(--lid); }
  .lid-rim { fill: var(--lid-rim); }
  .cup-body { fill: var(--cup-white); }
  .kraft-band { fill: var(--kraft); stroke: var(--kraft-edge); stroke-width: 1; }
  .brand-ring { fill: none; stroke: var(--ink); stroke-width: 1.5; }
  .brand-name { fill: var(--ink); font-family: "Hind", sans-serif; font-weight: 600; letter-spacing: 0.08em; }
  .size-name { fill: var(--ink); font-family: "Hind", sans-serif; font-weight: 400; }
  .size-name .strong { font-weight: 700; }
  .net-weight { fill: var(--ink); font-family: "Hind", sans-serif; font-weight: 700; letter-spacing: 0.02em; }
</style>
</head>
<body>
<svg class="cup-lineup" viewBox="0 0 1200 960" xmlns="http://www.w3.org/2000/svg">

  <!-- Tall-heron, 12 oz -->
  <g class="cup cup--tall">
    <polygon class="cup-body" points="114,310 430,310 380,841 156,841"/>
    <polygon class="kraft-band" points="117,340 427,340 383,797 153,797"/>
    <rect class="lid-dome" x="122" y="253" width="293" height="34" rx="8"/>
    <rect class="lid-rim" x="95" y="282" width="345" height="36" rx="10"/>
    <circle class="brand-ring" cx="199" cy="589" r="7"/>
    <text class="brand-name" x="212" y="594" font-size="14">KELMO Coffee</text>
    <text class="size-name" x="268" y="638" font-size="50" text-anchor="middle"><tspan class="strong">tall</tspan>heron</text>
    <text class="net-weight" x="268" y="665" font-size="11" text-anchor="middle">NET WEIGHT: 12 OZ</text>
  </g>

  <!-- Mid-Wren, 8 oz -->
  <g class="cup cup--mid">
    <polygon class="cup-body" points="517,460 790,460 762,824 545,824"/>
    <polygon class="kraft-band" points="519,486 788,486 764,795 543,795"/>
    <rect class="lid-dome" x="512" y="395" width="268" height="40" rx="8"/>
    <rect class="lid-rim" x="504" y="430" width="298" height="32" rx="10"/>
    <circle class="brand-ring" cx="597" cy="629" r="6"/>
    <text class="brand-name" x="608" y="634" font-size="12.5">KELMO Coffee</text>
    <text class="size-name" x="654" y="682" font-size="44" text-anchor="middle"><tspan class="strong">mid</tspan>wren</text>
    <text class="net-weight" x="654" y="704" font-size="9.5" text-anchor="middle">NET WEIGHT: 8 OZ</text>
  </g>

  <!-- Tiny-Lark, 6 oz -->
  <g class="cup cup--tiny">
    <polygon class="cup-body" points="888,611 1097,611 1078,822 908,822"/>
    <polygon class="kraft-band" points="890,624 1096,624 1080,799 906,799"/>
    <rect class="lid-dome" x="888" y="546" width="207" height="38" rx="8"/>
    <rect class="lid-rim" x="872" y="580" width="242" height="33" rx="10"/>
    <circle class="brand-ring" cx="950" cy="725" r="5"/>
    <text class="brand-name" x="959" y="729" font-size="10.5">KELMO Coffee</text>
    <text class="size-name" x="994" y="762" font-size="34" text-anchor="middle"><tspan class="strong">tiny</tspan>lark</text>
    <text class="net-weight" x="994" y="777" font-size="7.5" text-anchor="middle">NET WEIGHT: 6 OZ</text>
  </g>

</svg>
</body>
</html>
```